Website for keystone mobile detailing.

Need a homepage, pages for: car and truck detailing, boat detailing, airplane detailing, about us, contact us. I have the domain name through nimbuspark so I will need the design uploaded on my domain. Also hoping to link other domains to this page.I would like to see the logo more pronounced. I would like to see a large phone number link to call my business. The layout looks nice but the pics need to depict car washing and waxing not car mechanics. i would like the colors of the webpage to incorporate the colors found in the logo in some way. I would like links to social media pages

Target Market(s)

Local customers in Vero Beach, Florida.

Number of Pages Required

5+ page

Colors

Designer to choose colors to be used in the design.

Requirements
Must have
• Easy to navigate, attractive pages with pictures and logo, professional looking. must have my phone number and logo very prevalent and links to call or go to home page. I would like links to my social media accounts on the home page.
Nice to have
• Easy to navigate, attractive pages with pictures and logo, professional looking.

```html
<!DOCTYPE html>
<html lang="en">
<head>
<meta charset="utf-8">
<title>Keystone Mobile Detailing</title>
<link href="https://fonts.googleapis.com/css2?family=Roboto:wght@300;400;500;700&display=swap" rel="stylesheet">
<style>
:root{
  --red:#e8202a;
  --red-dark:#c4141d;
  --blue:#2aa6de;
  --ink:#222;
  --body:#444;
  --muted:#888;
  --white:#fff;
  --dark:#1c1c1e;
  --footer:#111214;
  --light:#f4f5f6;
}
*{box-sizing:border-box;margin:0;padding:0}
html,body{width:1200px;height:3529px;overflow:hidden}
body{font-family:'Roboto',Arial,sans-serif;color:var(--body);background:var(--white);position:relative}
section,header,footer,nav{position:absolute;left:0;width:1200px}
.abs{position:absolute}
.btn{position:absolute;background:var(--red);color:var(--white);border-radius:20px;font-size:13px;font-weight:500;text-transform:uppercase;display:flex;align-items:center;justify-content:center;letter-spacing:.3px}
.heading{position:absolute;left:0;width:1200px;text-align:center;font-size:33px;font-weight:400;color:var(--ink);text-transform:uppercase}
.heading::after{content:"";display:block;width:72px;height:3px;background:var(--blue);margin:12px auto 0}
.heading.light{color:var(--white)}

/* header */
.site-header{top:0;height:89px;background:var(--white)}
.brand{left:89px;top:14px;display:flex;align-items:center;gap:12px}
.brand-mark{width:46px;height:46px;border-radius:50%;background:var(--blue)}
.brand-name{font-size:26px;font-weight:700;color:var(--blue);line-height:1}
.call-bar{right:0;top:0;width:494px;height:33px;background:var(--red);clip-path:polygon(0 0,100% 0,100% 100%,28px 100%);display:flex;align-items:center;padding-left:165px;gap:12px;color:var(--white);font-size:22px;letter-spacing:1px}
.main-nav{top:89px;height:29px;background:var(--red);display:flex;align-items:center;font-size:12px;font-weight:500;color:var(--white);text-transform:uppercase}
.main-nav span{position:absolute}

/* hero */
.hero{top:118px;height:435px}
.hero-photo{position:absolute;inset:0;background:linear-gradient(100deg,#2a2c30 0%,#55585e 45%,#3a3c40 70%,#1e2023 100%)}
.hero-kicker{top:228px;left:0;width:1200px;text-align:center;color:var(--white);font-size:20px}
.hero-title{top:270px;left:0;width:1200px;text-align:center;color:var(--white);font-size:40px;font-weight:400;line-height:54px}
.dots{display:flex;gap:7px}
.dots i{width:11px;height:11px;border-radius:50%;background:var(--white);display:block}
.dots i.on{background:transparent;border:2px solid var(--white)}

/* about */
.about{top:553px;height:489px;background:linear-gradient(180deg,var(--white) 0%,#f1f2f3 100%)}
.photo{position:absolute;box-shadow:0 3px 8px rgba(0,0,0,.35);border:3px solid var(--white)}
.about h2{position:absolute;left:525px;top:67px;font-size:32px;font-weight:400;color:var(--ink)}
.about h2::after{content:"";display:block;width:60px;height:3px;background:var(--blue);margin-top:10px}
.about p{position:absolute;left:525px;top:140px;width:595px;font-size:13px;line-height:23px;color:var(--body)}

/* services */
.services{top:1042px;height:377px;background:linear-gradient(120deg,#3b3d40,#26282b 55%,#37393c)}
.service{position:absolute;width:240px;text-align:center}
.service .ring{width:128px;height:128px;border-radius:50%;border:2px solid var(--white);margin:0 auto;display:flex;align-items:center;justify-content:center;background:rgba(0,0,0,.15)}
.service .label{margin-top:12px;display:inline-block;color:var(--white);font-size:12px;font-weight:700;text-transform:uppercase;border-bottom:1px solid var(--white);padding:0 10px 3px}

/* testimonials */
.customers{top:1419px;height:522px;background:var(--white)}
.quote-box{left:146px;top:209px;width:906px;height:236px;border:2px solid #f3b8bb}
.avatar{left:541px;top:153px;width:118px;height:118px;border-radius:50%;background:linear-gradient(160deg,#c9ccd0,#8d96a0);border:4px solid var(--white);box-shadow:0 0 0 2px #ddd}
.qmark{font-size:80px;color:#d8d8d8;font-family:Georgia,serif;line-height:1;background:var(--white);padding:0 14px}
.quote-text{left:225px;top:290px;width:750px;text-align:center;font-size:13px;line-height:25px;color:var(--body)}
.vdots{display:flex;flex-direction:column;gap:9px}
.vdots i{width:9px;height:9px;border-radius:50%;background:#ccc;display:block}
.vdots i.on{background:transparent;border:2px solid #aaa}

/* contact */
.contact{top:1941px;height:457px;background:linear-gradient(110deg,#1e1f22 0%,#3c3f44 40%,#26282b 75%,#151617 100%)}
.field{position:absolute;border-bottom:1px solid rgba(255,255,255,.7);color:var(--white);font-size:12px;text-transform:uppercase;padding-bottom:5px}

/* blog */
.blog{top:2398px;height:736px;background:var(--white)}
.card{position:absolute;top:174px;width:325px;height:421px;background:var(--white);box-shadow:0 2px 8px rgba(0,0,0,.25)}
.card .thumb{height:207px}
.card h3{margin-top:28px;text-align:center;font-size:15px;font-weight:400;color:var(--ink);text-transform:uppercase}
.card p{margin:14px 18px 0;text-align:center;font-size:12.5px;line-height:22px;color:var(--body)}
.meta{display:flex;justify-content:center;gap:18px;margin-top:18px;font-size:12px;color:var(--body)}
.meta span{display:flex;align-items:center;gap:6px}

/* footer */
.site-footer{top:3134px;height:395px;background:linear-gradient(180deg,#1b1c1f,var(--footer))}
.site-footer h4{position:absolute;top:45px;color:var(--white);font-size:14px;font-weight:700;text-transform:uppercase}
.foot-line{position:absolute;color:var(--white);font-size:12.5px}
.quick{position:absolute;left:532px;top:88px;list-style:none;color:var(--white);font-size:12.5px;text-transform:uppercase}
.quick li{height:42px;display:flex;align-items:flex-start;gap:10px}
.quick li::before{content:"";width:5px;height:5px;border-radius:50%;background:var(--red);margin-top:5px}
.socials{left:875px;top:94px;display:flex;gap:17px}
.socials a{width:40px;height:40px;border:1.5px solid var(--white);display:block}
.copyright{left:0;top:3473px;width:1200px;border-top:1px solid #333;text-align:center;padding-top:16px;color:#ccc;font-size:12px}
</style>
</head>
<body>

<header class="site-header">
  <div class="brand abs">
    <span class="brand-mark"></span>
    <span class="brand-name">Keystone Mobile Detailing</span>
  </div>
  <a class="call-bar abs" href="tel:5550142290">
    <svg width="22" height="22" viewBox="0 0 24 24" fill="none" stroke="#fff" stroke-width="1.8"><path d="M6 3l3 0 2 5-2 1.5a11 11 0 0 0 5.5 5.5L16 13l5 2v3a2 2 0 0 1-2 2A16 16 0 0 1 4 5a2 2 0 0 1 2-2z"/></svg>
    555 - 014 - 2290
  </a>
</header>

<nav class="main-nav">
  <span style="left:193px">Home</span>
  <span style="left:275px">Car and Truck Detailing</span>
  <span style="left:492px">Boat Detailing</span>
  <span style="left:640px">Airplane Detailing</span>
  <span style="left:819px">About Us</span>
  <span style="left:929px">Contact Us</span>
</nav>

<section class="hero">
  <div class="hero-photo" role="img" aria-label="Close-up photo of a car being washed and polished"></div>
  <p class="hero-kicker abs" style="top:110px">Lorem Ipsum is simply dummy text of the print</p>
  <h1 class="hero-title abs" style="top:150px">Lorem Ipsum is simply dummy text of the<br>printing and typesetting industry.</h1>
  <a class="btn" style="left:475px;top:282px;width:247px;height:38px">Read More</a>
  <div class="dots abs" style="left:570px;top:387px"><i></i><i></i><i class="on"></i></div>
</section>

<section class="about">
  <div class="photo" role="img" aria-label="Hand spraying cleaner on a car" style="left:85px;top:59px;width:299px;height:341px;background:linear-gradient(140deg,#2d6fb0,#8fb5d8 50%,#3a5f8a)"></div>
  <div class="photo" role="img" aria-label="Foam-covered blue car panel" style="left:292px;top:207px;width:204px;height:221px;background:linear-gradient(150deg,#c9d3e0,#3e5aa6 55%,#26337a)"></div>
  <h2>About Us</h2>
  <p>Lorem Ipsum is simply dummy text of the printing and typesetting industry. Lorem Ipsum has been the industry's standard dummy text ever since the 1500s, when an unknown printer took a galley of type and scrambled it to make a type specimen book. It has survived not only five centuries, but also the leap into electronic typesetting, remaining essentially unchanged. It was popularised in the 1960s with the release of Letraset sheets</p>
  <a class="btn" style="left:525px;top:278px;width:131px;height:37px">Read More</a>
</section>

<section class="services" role="img" aria-label="Background photo of sponge washing a car">
  <h2 class="heading light" style="top:72px">Our Services</h2>
  <div class="service" style="left:216px;top:153px">
    <div class="ring">
      <svg width="58" height="58" viewBox="0 0 48 48" fill="none" stroke="#fff" stroke-width="2"><path d="M10 16h10v-6h-6"/><path d="M20 10v-3"/><rect x="10" y="24" width="28" height="12" rx="3"/><path d="M14 24l3-7h14l3 7"/><circle cx="16" cy="36" r="3"/><circle cx="32" cy="36" r="3"/></svg>
    </div>
    <span class="label">Car and Truck Detailing</span>
  </div>
  <div class="service" style="left:480px;top:153px">
    <div class="ring">
      <svg width="62" height="62" viewBox="0 0 48 48" fill="none" stroke="#fff" stroke-width="2"><path d="M6 28h36l-5 8H11z"/><path d="M14 28v-6h16l6 6"/><path d="M18 22v-5h8v5"/><path d="M6 40c4 2 8 2 12 0s8-2 12 0 8 2 12 0"/></svg>
    </div>
    <span class="label">Boat Detailing</span>
  </div>
  <div class="service" style="left:744px;top:153px">
    <div class="ring">
      <svg width="62" height="62" viewBox="0 0 48 48" fill="none" stroke="#fff" stroke-width="2"><path d="M6 24h34a4 4 0 0 1 0 4H10z"/><path d="M20 24l-6-10h4l10 10"/><path d="M22 28l-4 10h4l8-10"/><circle cx="14" cy="36" r="2"/><circle cx="34" cy="36" r="2"/></svg>
    </div>
    <span class="label">Airplane Detailing</span>
  </div>
</section>

<section class="customers">
  <h2 class="heading" style="top:68px">Our Satisfied Customers</h2>
  <div class="quote-box abs"></div>
  <span class="qmark abs" style="left:285px;top:190px">&ldquo;</span>
  <span class="qmark abs" style="left:856px;top:408px">&rdquo;</span>
  <div class="avatar abs" role="img" aria-label="Customer portrait"></div>
  <p class="quote-text abs">Lorem Ipsum is simply dummy text of the printing and typesetting industry. Lorem Ipsum has been the industry's standard dummy text ever since the 1500s, when an unknown printer took a galley of type and scrambled it to make a type specimen book. It has survived not only five centuries, but also the leap into electronic typesetting, remaining essentially unchanged. It was popularised in the 1960s with the release of Letraset sheets</p>
  <p class="abs" style="left:0;width:1200px;top:396px;text-align:center;font-size:13px;color:var(--ink)">JOHN DOE</p>
  <p class="abs" style="left:0;width:1200px;top:418px;text-align:center;font-size:13px;color:var(--muted)">Lorem Ipsum is simply</p>
  <div class="vdots abs" style="left:1080px;top:238px"><i></i><i></i><i class="on"></i></div>
</section>

<section class="contact" role="img" aria-label="Background photo of a headlight being machine polished">
  <h2 class="heading light" style="top:70px">Contact Us</h2>
  <div class="field" style="left:261px;top:155px;width:325px;font-size:10px">Name *<br>&nbsp;</div>
  <div class="field" style="left:612px;top:168px;width:325px">Email</div>
  <div class="field" style="left:261px;top:208px;width:676px;height:120px">Message</div>
  <a class="btn" style="left:525px;top:358px;width:131px;height:35px">Send Message</a>
</section>

<section class="blog">
  <h2 class="heading" style="top:66px">Our Blog</h2>
  <article class="card" style="left:87px">
    <div class="thumb" role="img" aria-label="White car covered in wash foam" style="background:linear-gradient(135deg,#6b5a4e,#d9d6d2 50%,#8a7465)"></div>
    <h3>Lorem Ipsum is simply dummy</h3>
    <p>Lorem Ipsum is simply dummy text of the printing and typesetting industry. Lorem Ipsum has been the industry's standard dummy text ever since the 1500s, when an unknown printer took a.</p>
    <div class="meta">
      <span><svg width="12" height="12" viewBox="0 0 12 12" fill="none" stroke="#f0a020"><rect x="1" y="2" width="10" height="9"/><path d="M1 5h10"/></svg>24 May 2017</span>
      <span><svg width="12" height="12" viewBox="0 0 12 12" fill="#f0a020"><circle cx="6" cy="4" r="2.5"/><path d="M1 12a5 5 0 0 1 10 0z"/></svg>Admin</span>
      <span><svg width="12" height="12" viewBox="0 0 12 12" fill="#f0a020"><path d="M1 2h10v6H5l-3 3V8H1z"/></svg>0</span>
    </div>
  </article>
  <article class="card" style="left:438px">
    <div class="thumb" role="img" aria-label="Dark car being rinsed with water" style="background:linear-gradient(135deg,#1c2024,#6e767d 55%,#2a2e33)"></div>
    <h3>Lorem Ipsum is simply dummy</h3>
    <p>Lorem Ipsum is simply dummy text of the printing and typesetting industry. Lorem Ipsum has been the industry's standard dummy text ever since the 1500s, when an unknown printer took a.</p>
    <div class="meta">
      <span><svg width="12" height="12" viewBox="0 0 12 12" fill="none" stroke="#f0a020"><rect x="1" y="2" width="10" height="9"/><path d="M1 5h10"/></svg>24 May 2017</span>
      <span><svg width="12" height="12" viewBox="0 0 12 12" fill="#f0a020"><circle cx="6" cy="4" r="2.5"/><path d="M1 12a5 5 0 0 1 10 0z"/></svg>Admin</span>
      <span><svg width="12" height="12" viewBox="0 0 12 12" fill="#f0a020"><path d="M1 2h10v6H5l-3 3V8H1z"/></svg>0</span>
    </div>
  </article>
  <article class="card" style="left:788px">
    <div class="thumb" role="img" aria-label="Car being pressure washed outdoors" style="background:linear-gradient(180deg,#2f6fc4 0%,#8fa4b5 45%,#5a6168 100%)"></div>
    <h3>Lorem Ipsum is simply dummy</h3>
    <p>Lorem Ipsum is simply dummy text of the printing and typesetting industry. Lorem Ipsum has been the industry's standard dummy text ever since the 1500s, when an unknown printer took a.</p>
    <div class="meta">
      <span><svg width="12" height="12" viewBox="0 0 12 12" fill="none" stroke="#f0a020"><rect x="1" y="2" width="10" height="9"/><path d="M1 5h10"/></svg>24 May 2017</span>
      <span><svg width="12" height="12" viewBox="0 0 12 12" fill="#f0a020"><circle cx="6" cy="4" r="2.5"/><path d="M1 12a5 5 0 0 1 10 0z"/></svg>Admin</span>
      <span><svg width="12" height="12" viewBox="0 0 12 12" fill="#f0a020"><path d="M1 2h10v6H5l-3 3V8H1z"/></svg>0</span>
    </div>
  </article>
  <a class="btn" style="left:525px;top:635px;width:131px;height:35px">View More</a>
</section>

<footer class="site-footer">
  <h4 style="left:85px">Contacts</h4>
  <p class="foot-line" style="left:85px;top:91px">ADDRESS: Lorem Ipsum</p>
  <p class="foot-line" style="left:85px;top:133px">PHONES: 000 - 0000 - 0000 , 000 - 0000 - 0000</p>
  <p class="foot-line" style="left:85px;top:175px">HOURS: 7 days a week from 9:00 am to 7:00 pm</p>
  <p class="foot-line" style="left:85px;top:218px">E-MAIL: info@keystonedetail.com</p>
  <h4 style="left:532px">Quick Links</h4>
  <ul class="quick">
    <li>Home</li><li>Car and Truck Detailing</li><li>Boat Detailing</li><li>Airplane Detailing</li><li>About Us</li><li>Contact Us</li>
  </ul>
  <h4 style="left:875px">Follow Us</h4>
  <div class="socials abs">
    <a aria-label="Social page 1"></a><a aria-label="Social page 2"></a><a aria-label="Social page 3"></a><a aria-label="Social page 4"></a>
  </div>
</footer>
<p class="copyright abs">© 2018 Keystone Mobile Detailing. All Right Reserved.</p>

</body>
</html>
```